nestlybloom - Ballon Design

I need a Ballon designed. Please use the psb file ballon_template.psb as template.

I would like to have a ballon designed similar to the file "example.png".
instead of the lorna kin logo please use my attached logo "nestlybloom logo.ai"

The text should be the same " IT'S A MOM" but the logo should be different.

I should look like more elegant. should be also white background. But for the design feel free.

thanks.
Updates

Please also add the webpage "www.nestlybloom.eu" on the ballon design.

```html
<!DOCTYPE html>
<html lang="en">
<head>
<meta charset="UTF-8">
<title>nestlybloom – It's a Mom balloon</title>
<link rel="stylesheet" href="https://fonts.googleapis.com/css2?family=Bangers&family=Ubuntu:wght@400;500&display=swap">
<style>
  :root {
    --paper: #ffffff;
    --rose: #cd7f9c;
    --ink-blue: #4a68a3;
  }
  * { margin: 0; padding: 0; box-sizing: border-box; }
  html, body {
    width: 1200px;
    height: 1194px;
    overflow: hidden;
    background: var(--paper);
  }
  .balloon-face {
    position: relative;
    width: 1200px;
    height: 1194px;
    background: var(--paper);
  }
  .headline {
    position: absolute;
    left: 0;
    width: 100%;
    text-align: center;
    font-family: "Bangers", "Impact", sans-serif;
    color: var(--rose);
    line-height: 1;
  }
  .headline-small {
    top: 215px;
    font-size: 205px;
    letter-spacing: 6px;
    transform: rotate(-3deg);
  }
  .headline-big {
    top: 385px;
    font-size: 355px;
    letter-spacing: 14px;
    transform: rotate(-4deg);
  }
  .brand {
    position: absolute;
    top: 700px;
    left: 0;
    width: 100%;
    display: flex;
    justify-content: center;
    align-items: center;
    gap: 18px;
  }
  .brand-dot {
    width: 26px;
    height: 26px;
    border-radius: 50%;
    background: var(--rose);
  }
  .brand-name {
    font-family: "Ubuntu", sans-serif;
    font-weight: 500;
    font-size: 78px;
    color: var(--ink-blue);
    line-height: 1;
  }
  .web-address {
    position: absolute;
    top: 832px;
    left: 0;
    width: 100%;
    text-align: center;
    font-family: "Ubuntu", sans-serif;
    font-weight: 400;
    font-size: 30px;
    letter-spacing: 0.5px;
    color: var(--ink-blue);
  }
</style>
</head>
<body>
  <main class="balloon-face">
    <div class="headline headline-small">IT’S A</div>
    <div class="headline headline-big">MOM</div>
    <div class="brand">
      <span class="brand-dot"></span>
      <span class="brand-name">nestlybloom</span>
    </div>
    <div class="web-address">www.nestlybloom.eu</div>
  </main>
</body>
</html>
```